8 1/2 x 11 Flyer Design for Water Damage Restoration Company

Houston Texas based Water Damage Restoration company is needing a advertising flyer that highlights water damage and water extraction.

KESTRAL Emergency Services
52710 Harlow Crossing Suite G4
Houston, Texas 77193
713-846-5170
www.KESTRAL58129.example

Water Damage Restoration
Water Extraction
Mold Prevention
24/7/365
FREE Evaluations

Suggested photos to use:
Water Damage
Leaking Pipes
Water on floors and ground
Water pouring from ceilings
Technicians
Company Logo
Photos

Company Colors:
Orange and Blue

```html
<!DOCTYPE html>
<html lang="en">
<head>
<meta charset="utf-8">
<title>KESTRAL Emergency Services Flyer</title>
<link rel="stylesheet" href="https://fonts.googleapis.com/css2?family=Montserrat:wght@400;500;600;700;800;900&family=Oswald:wght@400;500&display=swap">
<style>
  :root{
    --orange:#ff7a00;
    --orange-light:#ffa000;
    --orange-deep:#ff6200;
    --blue:#1c418f;
    --blue-dark:#173a82;
    --blue-light:#2552a8;
    --cream:#ffe7c9;
    --white:#ffffff;
    --ink:#1c2a55;
    --stage:#e6e5e8;
  }
  *{box-sizing:border-box;margin:0;padding:0}
  html,body{width:723px;height:1200px;overflow:hidden;background:var(--stage)}
  .canvas{position:relative;width:723px;height:1200px;overflow:hidden;background:var(--stage)}
  .flyer{position:absolute;left:21.5px;top:158px;width:875px;height:1137px;transform:scale(.7771);transform-origin:0 0;
    overflow:hidden;background:var(--blue);font-family:"Montserrat",sans-serif;color:var(--white);box-shadow:0 14px 30px rgba(0,0,0,.35)}
  .backdrop{position:absolute;inset:0;width:875px;height:1137px}
  .abs{position:absolute}
  .brand-title{left:0;width:875px;top:22px;text-align:center;font-weight:900;font-size:86px;letter-spacing:2px;color:var(--blue);line-height:1}
  .brand-sub{left:0;width:875px;top:104px;text-align:center;font-family:"Oswald",sans-serif;font-weight:500;font-size:40px;letter-spacing:1px;line-height:1}
  .tagline{left:0;width:875px;top:153px;text-align:center;font-size:16px;font-weight:500;letter-spacing:.5px;line-height:21px}
  .tagline strong{font-weight:800}
  .credentials{left:318px;top:198px;width:238px;height:22px;border-radius:11px;background:var(--blue);border:1px solid #ffb35c;
    font-size:11px;font-weight:700;display:flex;align-items:center;justify-content:center;gap:4px}
  .credentials .tick{display:inline-block;width:9px;height:9px;border-radius:50%;background:var(--orange)}
  .service-line{left:0;width:875px;top:234px;text-align:center;font-family:"Oswald",sans-serif;font-size:20px;line-height:25px;color:var(--cream);letter-spacing:.3px}
  .availability{left:500px;top:664px;width:196px;height:56px}
  .services{left:60px;top:742px;display:flex;flex-direction:column;gap:22px}
  .service{display:flex;align-items:center;gap:20px;font-size:24px;font-weight:700;line-height:32px}
  .service svg{width:60px;height:66px;flex:none}
  .perks{left:372px;top:742px;width:420px;display:grid;grid-template-columns:198px 1fr;row-gap:10px;font-size:13px;font-weight:500}
  .perks li{list-style:none;display:flex;align-items:center;gap:6px}
  .perks li::before{content:"";width:10px;height:6px;border-left:2.5px solid var(--orange);border-bottom:2.5px solid var(--orange);transform:rotate(-45deg) translateY(-2px)}
  .rule{left:376px;top:801px;width:405px;border-top:1.5px dotted rgba(255,255,255,.7)}
  .offer{left:372px;top:806px;font-size:45px;font-weight:800;line-height:1;white-space:nowrap}
  .offer .free{color:var(--orange)}
  .van-photo{left:388px;top:866px;width:384px;height:142px;border-radius:6px;
    background:linear-gradient(100deg,#e9773f 0%,#d9dee8 55%,#4a5874 100%)}
  .footer{left:0;top:1015px;width:875px;height:122px;background:var(--white);color:var(--ink)}
  .contact{left:66px;top:34px;font-size:13px;line-height:18px}
  .contact .company{font-weight:700;color:var(--blue)}
  .contact .company em{font-style:normal;color:var(--orange)}
  .contact .addr{display:flex;gap:5px}
  .divider{top:30px;width:1.5px;height:56px;background:#9aa5bf}
  .phone{left:372px;top:24px;width:222px;height:34px;border-radius:17px;background:var(--orange);color:var(--white);
    font-size:23px;font-weight:800;display:flex;align-items:center;justify-content:center;gap:8px}
  .web{left:372px;top:68px;width:222px;text-align:center;font-size:15px;display:flex;align-items:center;justify-content:center;gap:4px}
  .web b{color:var(--blue);font-weight:700}
  .wordmark{left:650px;top:36px;display:flex;align-items:center;gap:8px;font-size:34px;font-weight:800;color:var(--blue);letter-spacing:1px}
  .wordmark i{width:14px;height:14px;border-radius:50%;background:var(--orange)}
</style>
</head>
<body>
<div class="canvas">
  <div class="flyer">
    <svg class="backdrop" viewBox="0 0 875 1137">
      <defs>
        <linearGradient id="orangeFill" x1="0" y1="0" x2="0" y2="1">
          <stop offset="0" stop-color="var(--orange-light)"/><stop offset="1" stop-color="var(--orange-deep)"/>
        </linearGradient>
        <linearGradient id="moldWall" x1="0" y1="0" x2="1" y2="1"><stop offset="0" stop-color="#e8e6e1"/><stop offset="1" stop-color="#b9b5aa"/></linearGradient>
        <linearGradient id="floodRoom" x1="0" y1="0" x2="0" y2="1"><stop offset="0" stop-color="#8d8a86"/><stop offset="1" stop-color="#6f8c88"/></linearGradient>
        <linearGradient id="leakCeiling" x1="0" y1="0" x2="0" y2="1"><stop offset="0" stop-color="#eeebe4"/><stop offset="1" stop-color="#c9c3bc"/></linearGradient>
        <linearGradient id="technician" x1="0" y1="0" x2="1" y2="1"><stop offset="0" stop-color="#ededeb"/><stop offset="1" stop-color="#9a9a98"/></linearGradient>
        <linearGradient id="floodBoots" x1="0" y1="0" x2="1" y2="1"><stop offset="0" stop-color="#2f3d50"/><stop offset="1" stop-color="#a88334"/></linearGradient>
      </defs>
      <rect width="875" height="1137" fill="url(#orangeFill)"/>
      <polygon points="0,250 437,687 875,250 875,1137 0,1137" fill="var(--blue)"/>
      <polygon points="875,420 875,760 640,560" fill="var(--blue-light)" opacity=".6"/>
      <polygon points="0,420 0,760 230,560" fill="var(--blue-dark)" opacity=".6"/>
      <g stroke="var(--white)" stroke-width="10">
        <polygon role="img" aria-label="Photo: mold stains on a damp wall corner" points="137,87 287,237 137,387 -13,237" fill="url(#moldWall)"/>
        <polygon role="img" aria-label="Photo: flooded living room" points="287,237 437,387 287,537 137,387" fill="url(#floodRoom)"/>
        <polygon role="img" aria-label="Photo: water leaking from ceiling into a bucket" points="437,387 587,537 437,687 287,537" fill="url(#leakCeiling)"/>
        <polygon role="img" aria-label="Photo: technician repairing a wall" points="587,237 737,387 587,537 437,387" fill="url(#technician)"/>
        <polygon role="img" aria-label="Photo: boots standing in flood water" points="737,87 887,237 737,387 587,237" fill="url(#floodBoots)"/>
      </g>
    </svg>

    <h1 class="abs brand-title">KESTRAL</h1>
    <p class="abs brand-sub">EMERGENCY SERVICES</p>
    <p class="abs tagline">IS THERE WHEN&nbsp; YOUR CLIENTS<br><strong>NEED HELP THE MOST!</strong></p>
    <p class="abs credentials"><span class="tick"></span>LICENSED | <span class="tick"></span>BONDED | <span class="tick"></span>INSURED</p>
    <p class="abs service-line">RESIDENTIAL &amp; COMMERCIAL<br>RESTORATION SERVICES</p>

    <svg class="abs availability" viewBox="0 0 196 56">
      <rect x="4" y="8" width="100" height="40" rx="20" fill="var(--white)" stroke="var(--orange)" stroke-width="2" stroke-dasharray="3 3"/>
      <rect x="96" y="6" width="94" height="44" rx="22" fill="var(--orange)"/>
      <text x="18" y="38" font-family="Montserrat,sans-serif" font-weight="800" font-style="italic" font-size="24" fill="var(--orange)">24/7</text>
      <circle cx="102" cy="28" r="15" fill="var(--white)" stroke="var(--blue)" stroke-width="2.5"/>
      <path d="M102 19v9l6 4" stroke="var(--blue)" stroke-width="2.5" fill="none" stroke-linecap="round"/>
      <text x="122" y="35" font-family="Montserrat,sans-serif" font-weight="800" font-style="italic" font-size="22" fill="var(--white)">365</text>
      <text x="150" y="46" font-family="Montserrat,sans-serif" font-weight="600" font-style="italic" font-size="8" fill="var(--blue)">Days</text>
    </svg>

    <ul class="abs services">
      <li class="service"><svg viewBox="0 0 60 66"><polygon points="30,2 57,17 57,49 30,64 3,49 3,17" fill="var(--orange)" stroke="var(--white)" stroke-width="3"/></svg><span>Water Damage<br>Restoration</span></li>
      <li class="service"><svg viewBox="0 0 60 66"><polygon points="30,2 57,17 57,49 30,64 3,49 3,17" fill="var(--orange)" stroke="var(--white)" stroke-width="3"/></svg><span>Water<br>Extraction</span></li>
      <li class="service"><svg viewBox="0 0 60 66"><polygon points="30,2 57,17 57,49 30,64 3,49 3,17" fill="var(--orange)" stroke="var(--white)" stroke-width="3"/></svg><span>Mold<br>Prevention</span></li>
    </ul>

    <ul class="abs perks">
      <li>A+ Rated Service Provider</li>
      <li>All Insurance Carriers Billing</li>
      <li>Certified Technicians</li>
      <li>Claimwise Invoices</li>
    </ul>
    <div class="abs rule"></div>
    <p class="abs offer"><span class="free">FREE</span> Evaluations</p>

    <div class="abs van-photo" role="img" aria-label="Photo: branded orange and white company service van"></div>

    <footer class="abs footer">
      <div class="abs contact">
        <p class="company">KESTRAL <em>Emergency Services</em></p>
        <p class="addr"><svg width="14" height="16" viewBox="0 0 14 16"><path d="M7 1a5 5 0 0 1 5 5c0 4-5 9-5 9S2 10 2 6a5 5 0 0 1 5-5z" fill="none" stroke="var(--orange)" stroke-width="1.6"/><circle cx="7" cy="6" r="1.8" fill="var(--orange)"/></svg><span>52710 Harlow Crossing Suite G4<br>Houston, Texas 77193</span></p>
      </div>
      <div class="abs divider" style="left:340px"></div>
      <p class="abs phone"><svg width="22" height="22" viewBox="0 0 22 22"><circle cx="11" cy="11" r="10" fill="var(--white)"/><path d="M7 6l2 0 1 3-1.5 1a7 7 0 0 0 3.5 3.5l1-1.5 3 1 0 2a1.5 1.5 0 0 1-1.5 1.5A10 10 0 0 1 5.5 7.5 1.5 1.5 0 0 1 7 6z" fill="var(--orange)"/></svg>713-846-5170</p>
      <p class="abs web"><svg width="13" height="15" viewBox="0 0 14 16"><path d="M7 1a5 5 0 0 1 5 5c0 4-5 9-5 9S2 10 2 6a5 5 0 0 1 5-5z" fill="none" stroke="var(--orange)" stroke-width="1.6"/><circle cx="7" cy="6" r="1.8" fill="var(--orange)"/></svg><span>www.<b>KESTRAL58129</b>.example</span></p>
      <div class="abs divider" style="left:625px"></div>
      <p class="abs wordmark"><i></i>KESTRAL</p>
    </footer>
  </div>
</div>
</body>
</html>
```